Letterhead & logo design project

We need a letterhead for a new company called Brackenwold Ltd a firm of Chartered Accountants and Chartered Tax Advisers based in Pangbourne, Berkshire
Updates
Please include the following:
Chartered Accountants and Chartered Tax Advisers
Industry/Entity Type
It Company
Requirements
Must have
- Must have director's name at the bottom of the letterhead. Must also contain some wording at the bottom of the page to be provided by the NPRFA at a later date

```html
<!DOCTYPE html>
<html lang="en">
<head>
<meta charset="utf-8">
<title>Brackenwold Ltd Letterhead</title>
<link href="https://fonts.googleapis.com/css2?family=EB+Garamond:wght@400;500&family=Arimo:wght@400&display=swap" rel="stylesheet">
<style>
  :root {
    --backdrop: #272727;
    --paper: #ffffff;
    --brand-blue: #0b5c96;
    --ink-blue: #1d4f86;
    --band-text: #ffffff;
  }
  * { margin: 0; padding: 0; box-sizing: border-box; }
  html, body {
    width: 1200px;
    height: 1140px;
    overflow: hidden;
    background: var(--backdrop);
  }
  .letterhead {
    position: absolute;
    left: 114px;
    top: 11px;
    width: 953px;
    height: 1117px;
    background: var(--paper);
  }
  .brand-mark {
    position: absolute;
    left: 58px;
    top: 58px;
    width: 80px;
    height: 80px;
    background: var(--brand-blue);
  }
  .brand-lockup {
    position: absolute;
    left: 164px;
    top: 50px;
  }
  .brand-name {
    display: inline-block;
    font-family: "EB Garamond", serif;
    font-weight: 400;
    font-size: 41px;
    line-height: 46px;
    font-variant: small-caps;
    color: var(--brand-blue);
    white-space: nowrap;
    padding-right: 2px;
    border-bottom: 1.5px solid var(--brand-blue);
  }
  .brand-tagline {
    margin: 4px 0 0 8px;
    font-family: "Arimo", sans-serif;
    font-size: 19px;
    line-height: 23px;
    color: var(--brand-blue);
    text-transform: uppercase;
  }
  .motto-band {
    position: absolute;
    left: 46px;
    top: 962px;
    width: 861px;
    height: 41px;
    background: var(--brand-blue);
    color: var(--band-text);
    font-family: "EB Garamond", serif;
    font-size: 25px;
    font-variant: small-caps;
    letter-spacing: 0.3px;
    display: flex;
    align-items: center;
    justify-content: center;
  }
  .contact-block {
    position: absolute;
    left: 0;
    top: 1008px;
    width: 953px;
    text-align: center;
    font-family: "EB Garamond", serif;
    color: var(--ink-blue);
  }
  .director-name { font-size: 21px; line-height: 26px; }
  .office-address { font-size: 15px; line-height: 21px; }
  .contact-lines { font-size: 15.5px; line-height: 21px; }
</style>
</head>
<body>
  <main class="letterhead">
    <div class="brand-mark" aria-hidden="true"></div>
    <div class="brand-lockup">
      <div class="brand-name">Brackenwold Ltd</div>
      <div class="brand-tagline">Chartered Accountants &amp;<br>Chartered Tax Advisers</div>
    </div>

    <div class="motto-band">Providing Solutions For Difficult Circumstances</div>

    <footer class="contact-block">
      <p class="director-name">Director's name</p>
      <p class="office-address">14 Mill Lane, Riverside Row, UK 4821</p>
      <p class="contact-lines">Tel.: (44)00-555-0142 l Fax: (44)00-555-0143 l Email: director@brackenwold.example</p>
    </footer>
  </main>
</body>
</html>
```